Business Card Design

I need a card design for Melbourne based business in Australia, called T W Concrete Services. We Concrete and excavate. Concreteing is main part of business.Commercial ,Residential and industrial.We want to be known as Tallowood (services) as form of abbreviation.We would like to highlight the initials with contact phone. A clean straight edge design. We have no color preference and would prefer a design that can easily be used on all parts of our business including clothing,vechiles and stationary

Industry/Entity Type

Business

Contact Information for Business Card

Colin 0491 570 156
Barry 0491 570 157
office@tallowood.example

```html
<!DOCTYPE html>
<html lang="en">
<head>
<meta charset="UTF-8">
<title>Tallowood – Business Card</title>
<link rel="stylesheet" href="https://fonts.googleapis.com/css2?family=Work+Sans:wght@300&display=swap">
<style>
  :root {
    --surround: #4a4a4c;
    --card-blue: #0a79be;
    --ink-white: #ffffff;
    --ink-soft: #e8f2fa;
  }
  html, body {
    margin: 0;
    padding: 0;
    width: 1200px;
    height: 740px;
    overflow: hidden;
    background: var(--surround);
    font-family: "Work Sans", sans-serif;
  }
  .canvas {
    position: relative;
    width: 1200px;
    height: 740px;
    background: var(--surround);
  }
  .card {
    position: absolute;
    left: 45px;
    top: 45px;
    width: 1112px;
    height: 650px;
    background: var(--card-blue);
    color: var(--ink-white);
  }
  .brand-name {
    position: absolute;
    left: 28px;
    top: 124px;
    margin: 0;
    font-weight: 300;
    font-size: 150px;
    line-height: 1;
    letter-spacing: -2px;
    white-space: nowrap;
  }
  .tagline {
    position: absolute;
    left: 31px;
    top: 266px;
    margin: 0;
    font-weight: 300;
    font-size: 29px;
    line-height: 1;
    color: var(--ink-soft);
    white-space: nowrap;
  }
  .contacts {
    position: absolute;
    left: 31px;
    top: 550px;
    margin: 0;
    display: grid;
    grid-template-columns: 163px auto;
    row-gap: 8px;
    font-weight: 300;
    font-size: 29px;
    line-height: 34px;
    color: var(--ink-soft);
  }
  .contacts dt, .contacts dd { margin: 0; white-space: nowrap; }
  .email {
    position: absolute;
    right: 36px;
    top: 566px;
    margin: 0;
    font-weight: 300;
    font-size: 29px;
    line-height: 34px;
    color: var(--ink-soft);
    white-space: nowrap;
  }
</style>
</head>
<body>
  <main class="canvas">
    <section class="card" aria-label="Tallowood business card">
      <h1 class="brand-name">Tallowood</h1>
      <p class="tagline">Commercial, Residential and Industrial Concreting</p>
      <dl class="contacts">
        <dt>Colin</dt><dd>0491 570 156</dd>
        <dt>Barry</dt><dd>0491 570 157</dd>
      </dl>
      <p class="email">office@tallowood.example</p>
    </section>
  </main>
</body>
</html>
```